Pure Palm tree rhum label design

We need a label design for a palm tree rhum named 'Voile Cendré'. We have an original design and we need an enhancement or a new design that reflects the product. It is a liquor. The label should be bilingual (French and English). We have original design that gives an idea and can be used as starting point. The text on the label for the existing design has to show up in the new design. The text is uploaded too as well as the existing design.
Update:
- The design must use Oil Palm Tree and not Palm Tree. Sample Images are attached.
- The neck of the bottle has to have the name of the product: Voile Cendré.
- The word 'Liqueur' goes between the volume (1L) and the percentage of alcohol (43% Vol).
- Back side text is provided: see document
- The following description goes between the English and the french version (front and back):
The word: L'Original
The representation of a palm oil tree
The word: Original.
An image is uploaded for that.
No mandatory Fonts or Color or Bakground.

Font styles to use
Serif
Sans Serif
Script

```html
<!DOCTYPE html>
<html lang="fr">
<head>
<meta charset="UTF-8">
<title>Voile Cendré – Sodabi rectifié</title>
<link rel="stylesheet" href="https://fonts.googleapis.com/css2?family=Federo&family=Great+Vibes&display=swap">
<style>
  :root {
    --page: #ffffff;
    --label: #000000;
    --emblem: #3b3b3b;
    --gold-light: #f6d24a;
    --gold-mid: #e0b422;
    --gold-deep: #b8870f;
    --script: #ffffff;
  }
  html, body {
    margin: 0;
    padding: 0;
    width: 1200px;
    height: 481px;
    overflow: hidden;
    background: var(--page);
  }
  .label {
    position: relative;
    width: 1200px;
    height: 481px;
  }
  .label-shape {
    position: absolute;
    inset: 0;
    display: block;
  }
  .brand-name {
    position: absolute;
    left: 0;
    width: 1200px;
    top: 246px;
    margin: 0;
    text-align: center;
    font-family: "Federo", sans-serif;
    font-weight: 400;
    font-size: 66px;
    line-height: 1;
    letter-spacing: 1px;
    background: linear-gradient(180deg, var(--gold-light) 0%, var(--gold-mid) 50%, var(--gold-deep) 100%);
    -webkit-background-clip: text;
    background-clip: text;
    color: transparent;
  }
  .product-type {
    position: absolute;
    left: 0;
    width: 1200px;
    top: 352px;
    margin: 0;
    text-align: center;
    font-family: "Great Vibes", cursive;
    font-size: 62px;
    line-height: 1;
    color: var(--script);
  }
</style>
</head>
<body>
  <div class="label">
    <svg class="label-shape" width="1200" height="481" viewBox="0 0 1200 481" xmlns="http://www.w3.org/2000/svg">
      <defs>
        <linearGradient id="gold-rule" x1="0" y1="0" x2="0" y2="1">
          <stop offset="0" stop-color="var(--gold-light)"/>
          <stop offset="0.5" stop-color="var(--gold-mid)"/>
          <stop offset="1" stop-color="var(--gold-deep)"/>
        </linearGradient>
      </defs>
      <path class="label-body" fill="var(--label)"
        d="M0,145 H330 C380,145 400,122 422,92 C470,24 540,2 600,2 C660,2 730,24 778,92 C800,122 820,145 870,145 H1200 V479 H0 Z"/>
      <rect class="oil-palm-emblem" role="img" aria-label="Oil palm tree emblem in dark grey"
        x="492" y="30" width="172" height="216" rx="40" fill="var(--emblem)"/>
      <rect class="gold-rule gold-rule--left" x="0" y="400" width="418" height="4" fill="url(#gold-rule)"/>
      <rect class="gold-rule gold-rule--right" x="780" y="400" width="420" height="4" fill="url(#gold-rule)"/>
    </svg>
    <h1 class="brand-name">Voile Cendré</h1>
    <p class="product-type">Sodabi rectifie</p>
  </div>
</body>
</html>
```